'The Marlowe Draft' needs a movie poster

We need a movie poster for our short film coming up.

Genre: Drama/Mystery

Plot/Synopsis:
The Marlowe Draft explores the fraught relationship between creation and destiny, the creator and the created: inspiration, obsession, destruction.
In the opening scene we are introduced to Conrad Marlowe and a young writer, Nora, whose stories play out decades apart and yet are intricately linked. Conrad struggles with a block during the writing of his first novel; Nora, obsessed with uncovering her own past is inexplicably drawn to Marlowe’s house and accepts a room for let from Wanda, a strange woman who also resides there. As the two woman avoid delving too deep into each other’s pasts, suspicious of their intentions, Nora discovers that Conrad mysteriously died without finishing his debut novel and Wanda is most certainly holding something back.
Tensions are raised as Nora settles into Conrad’s office and investigates the chattels left behind on his bureau. Accidentally marking a waiting page of manuscript, she unlocks a sixth sense of déjà vu, obsession seeps into possession and the voice of the author comes to life in an unexpected manner in order to enact his long awaited epilogue. With-in the novel, Nora finds the key to her past and confronts Wanda with what she uncovers.
Dealing with the dark and destructive side of creativity, The Marlowe Draft is an edgy mystery with a lurking subtext; Or is it just the greatest plot twist penned by a non-living author.

I have attached for you some images taken from the video camera.
Feel free to add any graphic if you want. I don't have a particular idea of how I want the poster so far so you are pretty free as long as The poster is appealing to the public and make them want to see the film and is related to the synopsis.

-An KorvaReel Production see our logo attached in the pictures
-Director by Matteo Lunardi
-screenplay by Dale Whitford

-Staring: (by order of importance)
Gina Marchetti
Lorna Tibbett
Colin Frame
Ross Dunmore

-Log line: Are you here to fill those pages?

Feel free to use any of those pictures or any of your design if you have ideas. Or even combine some of our pics with some design of yours.
Nora the lead actress is the young girl on the picture. she has to be in the poster. The other older woman is Wanda! She is the supporting role-an important key of the story but very mysterious. (she doesn’t have to be in the poster)

Also it is IMPORTANT for me to have this poster in a format that I can edit as I will need to add some more names in the crew & music credit. Important that you could make the changes for me too include in this price.

Target Market(s)

Film festivals

Industry/Entity Type

Movie

Colors

Designer to choose colors to be used in the design.

Requirements
Must have
• The lead Nora (the young girl) in the poster.
• The producer logo must appear.
• A good title writing style.
• Drama feel.
Nice to have
• It would be nice to incorporate a gun in the design of the title 'The Marlowe Draft'

```html
<!DOCTYPE html>
<html lang="en">
<head>
<meta charset="utf-8">
<title>The Marlowe Draft — Poster</title>
<link href="https://fonts.googleapis.com/css2?family=Montserrat:wght@600;700;800&display=swap" rel="stylesheet">
<style>
  :root {
    --page-bg: #e4e4e2;
    --paper: #f7f7f7;
    --paper-shade: #d9d9db;
    --ink: #1d2127;
    --ink-soft: #5b5f66;
    --accent: #d0141b;
    --light: #ffffff;
  }
  * { margin: 0; padding: 0; box-sizing: border-box; }
  html, body { width: 1200px; height: 820px; overflow: hidden; background: var(--page-bg); }
  body { font-family: "Montserrat", Arial, sans-serif; }

  .poster {
    position: absolute; left: 320px; top: 20px;
    width: 560px; height: 780px; overflow: hidden;
    background: radial-gradient(ellipse at 70% 55%, var(--paper) 0%, #ececee 55%, var(--paper-shade) 100%);
  }
  .poster-art { position: absolute; inset: 0; }

  .credit {
    position: absolute; top: 34px;
    color: var(--light); font-weight: 700; font-size: 11px;
    letter-spacing: 0.04em; line-height: 1.45; text-align: center;
  }
  .credit--director { left: 28px; width: 140px; }
  .credit--writer { left: 180px; width: 130px; }

  .studio {
    position: absolute; top: 120px; left: 360px; width: 170px;
    display: flex; align-items: center; justify-content: center; gap: 8px;
  }
  .studio-mark { width: 14px; height: 14px; background: var(--accent); }
  .studio-name { font-weight: 700; font-size: 20px; color: var(--ink); letter-spacing: 0.02em; }

  .cast {
    position: absolute; top: 218px; left: 370px; width: 150px;
    list-style: none; text-align: center;
  }
  .cast li {
    color: var(--ink); font-weight: 700; font-size: 13px; letter-spacing: 0.03em;
    padding: 10px 0 11px;
  }
  .cast li + li { border-top: 1px dashed var(--ink-soft); }

  .title {
    position: absolute; left: 0; top: 380px; width: 560px;
    font-weight: 800; color: var(--light); line-height: 0.9;
  }
  .title-line { display: block; white-space: nowrap; }
  .title-the { font-size: 62px; padding-left: 208px; }
  .title-name { font-size: 74px; padding-left: 96px; letter-spacing: -0.01em; }
  .title-draft { font-size: 92px; padding-left: 220px; letter-spacing: -0.01em; }
  .title-accent { color: var(--accent); }

  .tagline {
    position: absolute; top: 664px; left: 292px; width: 170px;
    font-weight: 700; font-size: 16px; line-height: 1.3; color: var(--light);
    white-space: nowrap;
  }
  .tagline span { display: block; }
  .tagline .line-2 { padding-left: 46px; font-size: 19px; }
  .tagline .line-3 { padding-left: 22px; color: var(--accent); font-size: 15px; }
</style>
</head>
<body>
  <main class="poster">
    <svg class="poster-art" width="560" height="780" viewBox="0 0 560 780">
      <defs>
        <linearGradient id="sceneTone" x1="0" y1="0" x2="0.4" y2="1">
          <stop offset="0" stop-color="#3b4250"/>
          <stop offset="0.35" stop-color="#6a5448"/>
          <stop offset="0.6" stop-color="#2a2d34"/>
          <stop offset="1" stop-color="#121419"/>
        </linearGradient>
        <linearGradient id="steelTone" x1="0" y1="0" x2="1" y2="1">
          <stop offset="0" stop-color="#9ea1a9" stop-opacity="0.85"/>
          <stop offset="1" stop-color="#55585f" stop-opacity="0.85"/>
        </linearGradient>
      </defs>
      <path role="img" aria-label="Photograph: Nora with arms raised in front of the Marlowe house at dusk, in a dark dress"
        fill="url(#sceneTone)"
        d="M0,0 L300,0 L312,34 L302,72 L326,118 L316,176 L342,228 L330,282 L360,332 L368,398 L392,452 L384,520 L410,572 L440,622 L452,700 L470,780
           L246,780 L250,700 L244,640 L210,580 L160,540 L118,470 L84,392 L52,300 L34,236 L20,170 L0,150 Z"/>
      <rect role="img" aria-label="Illustration: silver revolver held low in Nora's hand"
        x="150" y="560" width="96" height="196" rx="10" fill="url(#steelTone)"/>
    </svg>

    <p class="credit credit--director">DIRECTOR BY<br>MATTEO LUNARDI</p>
    <p class="credit credit--writer">SCREENPLAY BY<br>DALE WHITFORD</p>

    <div class="studio">
      <span class="studio-mark"></span>
      <span class="studio-name">KorvaReel</span>
    </div>

    <ul class="cast">
      <li>GINA MARCHETTI</li>
      <li>LORNA TIBBETT</li>
      <li>COLIN FRAME</li>
      <li>ROSS DUNMORE</li>
    </ul>

    <h1 class="title">
      <span class="title-line title-the">THE</span>
      <span class="title-line title-name">MAR<span class="title-accent">LOWE</span></span>
      <span class="title-line title-draft">DR<span class="title-accent">AFT</span></span>
    </h1>

    <p class="tagline">
      <span class="line-1">ARE YOU HERE</span>
      <span class="line-2">TO FILL</span>
      <span class="line-3">THOSE PAGES?</span>
    </p>
  </main>
</body>
</html>
```